Business cards

I would like a black background with the design I previously chose. I need 2 sets of cards. Mine will have Marisol Brandt, Broker/Owner, 307-555-0148 and marisol.harborpeak@mailvista.com
The second set will read, Dana Rutledge, Realtor 307-555-0172, dana.harborpeak@mailvista.com

Industry/Entity Type

Business

```html
<!DOCTYPE html>
<html lang="en">
<head>
<meta charset="utf-8">
<title>Business Cards – Marisol Brandt &amp; Dana Rutledge</title>
<link rel="stylesheet" href="https://fonts.googleapis.com/css2?family=Cormorant+Garamond:wght@500&family=Lato:wght@400&display=swap">
<style>
  :root {
    --backdrop: #d9d6d4;
    --card-dark: #1f1f1f;
    --card-mid: #343434;
    --accent-red: #b3221f;
    --accent-red-deep: #5e0e0c;
    --text-light: #e9e6e2;
    --text-muted: #c9c4be;
    --rule: #a9a49e;
  }
  * { box-sizing: border-box; margin: 0; padding: 0; }
  html, body { width: 805px; height: 1200px; overflow: hidden; }
  body { background: var(--backdrop); position: relative; }

  .business-card {
    position: absolute;
    left: 40px;
    width: 717px;
    height: 425px;
    background: radial-gradient(ellipse at 50% 30%, var(--card-mid) 0%, var(--card-dark) 75%);
    box-shadow: 0 4px 10px rgba(0,0,0,0.35);
    overflow: hidden;
  }
  .business-card--broker { top: 126px; }
  .business-card--realtor { top: 586px; }

  .edge-band {
    position: absolute;
    left: 0; top: 0;
    width: 22px; height: 100%;
    background: linear-gradient(90deg, var(--accent-red-deep), var(--accent-red) 60%, var(--accent-red-deep));
  }
  .side-tab {
    position: absolute;
    right: 0;
    width: 22px;
    background: linear-gradient(180deg, var(--accent-red) 0%, var(--accent-red-deep) 100%);
  }
  .business-card--broker .side-tab { top: 129px; height: 188px; }
  .business-card--realtor .side-tab { top: 106px; height: 193px; }

  .identity {
    position: absolute;
    left: 0; right: 0;
    top: 200px;
    text-align: center;
  }
  .business-card--realtor .identity { top: 178px; }
  .identity__name {
    font-family: "Cormorant Garamond", serif;
    font-variant: small-caps;
    font-weight: 500;
    font-size: 30px;
    letter-spacing: 1px;
    color: var(--text-light);
    line-height: 1;
  }
  .identity__rule {
    width: 295px;
    height: 1px;
    margin: 10px auto 12px;
    background: linear-gradient(90deg, transparent, var(--rule) 20%, var(--rule) 80%, transparent);
  }
  .identity__title {
    font-family: "Lato", sans-serif;
    font-size: 15px;
    color: var(--text-muted);
  }

  .contact-row {
    position: absolute;
    left: 0; right: 0;
    top: 348px;
    display: flex;
    align-items: center;
    justify-content: center;
    gap: 14px;
    font-family: "Cormorant Garamond", serif;
    font-size: 15px;
    color: var(--text-muted);
  }
  .business-card--realtor .contact-row { top: 345px; }
  .contact-row__icon { width: 26px; height: 20px; flex: none; }
  .contact-row__divider {
    width: 2px; height: 40px;
    background: var(--text-light);
    margin: 0 8px;
  }
</style>
</head>
<body>

  <section class="business-card business-card--broker">
    <div class="edge-band"></div>
    <div class="side-tab"></div>
    <div class="identity">
      <h1 class="identity__name">Marisol Brandt</h1>
      <div class="identity__rule"></div>
      <p class="identity__title">Broker/Owner</p>
    </div>
    <div class="contact-row">
      <svg class="contact-row__icon" viewBox="0 0 26 20" aria-hidden="true">
        <rect x="1" y="2" width="24" height="16" fill="#b3221f"/>
        <path d="M1 2 L13 11 L25 2" fill="none" stroke="#1f1f1f" stroke-width="1.6"/>
      </svg>
      <span class="contact-row__email">marisol.harborpeak@mailvista.com</span>
      <span class="contact-row__divider"></span>
      <svg class="contact-row__icon" viewBox="0 0 26 20" aria-hidden="true">
        <path d="M6 2 C3 4 3 8 7 12 C11 17 15 19 19 17 L20 14 L16 11 L14 13 C12 12 9 9 8 7 L10 5 L8 1 Z" fill="#b3221f"/>
      </svg>
      <span class="contact-row__phone">307-555-0148</span>
    </div>
  </section>

  <section class="business-card business-card--realtor">
    <div class="edge-band"></div>
    <div class="side-tab"></div>
    <div class="identity">
      <h1 class="identity__name">Dana Rutledge</h1>
      <div class="identity__rule"></div>
      <p class="identity__title">Realtor</p>
    </div>
    <div class="contact-row">
      <svg class="contact-row__icon" viewBox="0 0 26 20" aria-hidden="true">
        <rect x="1" y="2" width="24" height="16" fill="#b3221f"/>
        <path d="M1 2 L13 11 L25 2" fill="none" stroke="#1f1f1f" stroke-width="1.6"/>
      </svg>
      <span class="contact-row__email">dana.harborpeak@mailvista.com</span>
      <span class="contact-row__divider"></span>
      <svg class="contact-row__icon" viewBox="0 0 26 20" aria-hidden="true">
        <path d="M6 2 C3 4 3 8 7 12 C11 17 15 19 19 17 L20 14 L16 11 L14 13 C12 12 9 9 8 7 L10 5 L8 1 Z" fill="#b3221f"/>
      </svg>
      <span class="contact-row__phone">307-555-0172</span>
    </div>
  </section>

</body>
</html>
```